Flyer-Design für Pilzzucht
Zielgruppe
Wir sind ein Pilzzucht-Unternehmen, und vertreiben Pilzkulturen und Zubehör, mit dem Hobby-Pilzzüchter zuhause ihre eigenen Pilze anbauen können.
Die Zielgruppe sind Menschen, die gerne etwas selbst herstellen, selbst anbauen und mit ihren eigenen Händen machen möchten. Meistens sind solche Menschen auch naturverbunden oder vielseitig interessiert.
Aufgabenstellung
Das Design sollte sich grob an der Farbgebung der Internetseite www.moosgarten-kultur.shop orientieren. Es soll nicht zu dunkel sein, natürlich und frisch wirken. Der Flyer ist zur Neukundengewinnung gedacht und soll das Interesse am Pilze Züchten und an unseren Produkten wecken. Die Hochwertigkeit der angebotenen Produkte soll erkennbar sein. Wir haben keine Massenproduktion sondern produzieren handwerklich und mit Sorgfalt.
Wir haben noch kein finales Logo, deshalb nutzen wir als Logo-Ersatz unsere Domain www.moosgarten-kultur.shop in der Schriftart Atlanta.
Bitte integrieren Sie einen Gutscheincode, der einen Rabatt für Neukunden bzw. einen Gutschein für kostenlosen Versand enthält.
Vom Format her können Sie klassische Postkartenformate oder auch A5 wählen, je nachdem, wieviel Platz Ihr Design benötigt, oder Sie machen einen Vorschlag.

```html
<!DOCTYPE html>
<html lang="de">
<head>
<meta charset="utf-8">
<title>Flyer Pilzkulturen &amp; Zubehör – Präsentation</title>
<link href="https://fonts.googleapis.com/css2?family=Work+Sans:wght@400;500;600;700&family=Amatic+SC:wght@400;700&display=swap" rel="stylesheet">
<style>
  :root{
    --board:#ececec;
    --cream:#fbf8f0;
    --brown:#4a2e12;
    --green-light:#8db236;
    --green:#6f9a22;
    --green-dark:#4a6d16;
    --yellow:#f2c500;
    --badge-ink:#3d7a14;
    --label:#9a9a9a;
    --ink:#222;
  }
  *{margin:0;padding:0;box-sizing:border-box}
  html,body{width:1200px;height:2452px;overflow:hidden}
  body{position:relative;background:var(--board);font-family:"Work Sans",Arial,sans-serif;color:var(--ink)}
  .sheet-divider{position:absolute;left:0;top:853px;width:1200px;height:21px;background:#fff}
  .section-title{position:absolute;left:29px;font-size:22px;font-weight:400;color:#1c1c1c}
  .variant-label{position:absolute;font-size:21px;color:var(--label);line-height:29px;letter-spacing:.3px}

  .card{position:absolute;width:398px;height:566px;background:var(--cream);overflow:hidden;box-shadow:0 1px 4px rgba(0,0,0,.18)}
  .brand{position:absolute;top:26px;left:32px;display:flex;align-items:center;gap:8px;font-weight:700;font-size:18px;color:var(--brown);white-space:nowrap;z-index:3}
  .brand--right{left:auto;right:34px}
  .brand-dot{width:12px;height:12px;border-radius:50%;background:var(--brown)}

  .photo{position:absolute;left:34px;top:69px;width:330px;height:372px}
  .photo--porcini{background:
      linear-gradient(180deg,rgba(0,0,0,0) 70%,rgba(60,45,30,.35) 100%),
      linear-gradient(135deg,#a39e90 0%,#7d766a 18%,#9a6a3e 32%,#e2d6c4 44%,#8a5a32 55%,#3a2c20 68%,#b47a48 80%,#4a3626 100%)}
  .photo--shimeji{background:
      linear-gradient(160deg,rgba(255,255,255,0) 35%,rgba(233,226,210,.55) 55%,rgba(255,255,255,0) 75%),
      linear-gradient(180deg,#c49a6c 0%,#b98c5e 40%,#c8a27a 70%,#b3875a 100%)}
  .photo--forest{background:
      linear-gradient(100deg,rgba(0,0,0,0) 50%,rgba(214,204,196,.5) 78%,rgba(0,0,0,0) 100%),
      linear-gradient(180deg,#5d6a4a 0%,#3f4b35 30%,#6b4e34 48%,#4a5a3c 62%,#8d9a9e 80%,#6f7d72 100%)}
  .photo--chanterelle{background:
      linear-gradient(170deg,rgba(0,0,0,0) 30%,rgba(226,150,60,.55) 48%,rgba(0,0,0,0) 62%),
      linear-gradient(180deg,#22301f 0%,#5d4a3e 28%,#c29a82 45%,#a88470 60%,#2d3b28 85%,#1f2a1f 100%)}
  .photo--oyster{background:linear-gradient(180deg,#ebe6dc 0%,#dcd2c0 30%,#c9bda8 50%,#8e8070 64%,#2a2624 78%,#141414 100%)}

  .meadow{position:absolute;left:0;bottom:0;width:398px;height:172px;z-index:1}
  .headline{position:absolute;left:0;width:398px;top:464px;text-align:center;color:#fff;font-weight:600;font-size:26px;letter-spacing:.2px;z-index:2;text-shadow:0 1px 3px rgba(0,0,0,.25)}
  .subline{position:absolute;left:0;width:398px;top:503px;text-align:center;color:#fff;font-size:16px;letter-spacing:.8px;z-index:2}

  .badge{position:absolute;width:100px;height:100px;margin:-50px 0 0 -50px;border-radius:50%;background:var(--yellow);display:flex;align-items:center;justify-content:center;z-index:4}
  .badge span{font-family:"Amatic SC",cursive;font-weight:700;color:var(--badge-ink);font-size:17px;line-height:18px;text-align:center;transform:rotate(-8deg)}

  /* back side */
  .intro{position:absolute;left:34px;width:180px;font-size:8px;line-height:12.5px;color:var(--brown)}
  .tile{position:absolute}
  .tile--sets{left:230px;top:125px;width:168px;height:196px;background:linear-gradient(180deg,#f4f2ee 0%,#9a948a 25%,#6e6a62 45%,#c8c4bc 62%,#4a4744 82%,#3c3936 100%)}
  .tile--substrate{left:34px;top:275px;width:189px;height:145px;background:
      linear-gradient(90deg,rgba(0,0,0,0) 30%,rgba(28,22,18,.85) 45%,rgba(28,22,18,.85) 62%,rgba(0,0,0,0) 78%),
      linear-gradient(180deg,#4d6f92 0%,#3c5877 55%,#2f2b28 100%)}
  .tile--garden{left:230px;top:328px;width:134px;height:155px;background:linear-gradient(180deg,#2c3a26 0%,#5a6b3a 30%,#8d5a3a 52%,#d8c8b0 68%,#6d7f43 82%,#394a2a 100%)}
  .tag{position:absolute;height:22px;padding:0 20px 0 10px;background:var(--green);color:#fff;font-size:10.5px;line-height:22px;white-space:nowrap;clip-path:polygon(0 0,100% 0,calc(100% - 10px) 50%,100% 100%,0 100%);z-index:2}
  .offer{position:absolute;left:32px;top:436px;font-family:"Amatic SC",cursive;font-weight:400;font-size:37px;line-height:33px;color:var(--green)}
  .offer-terms{position:absolute;left:34px;top:508px;width:186px;font-size:6px;line-height:8px;color:var(--green-dark)}
</style>
</head>
<body>

<h2 class="section-title" style="top:33px">Vorder- und Rückseite DIN A5</h2>

<section class="card" style="left:162px;top:144px">
  <div class="brand"><span class="brand-dot"></span>moosgarten-kultur.shop</div>
  <div class="photo photo--porcini" role="img" aria-label="Steinpilze auf Leinentuch"></div>
  <svg class="meadow" viewBox="0 0 398 172" preserveAspectRatio="none" aria-hidden="true">
    <defs><linearGradient id="g1" x1="0" y1="0" x2="0" y2="1"><stop offset="0" stop-color="#8db236"/><stop offset="1" stop-color="#4a6d16"/></linearGradient></defs>
    <path d="M0 12 C90 -4 170 28 260 16 C320 8 370 6 398 12 L398 172 L0 172Z" fill="url(#g1)" opacity=".82"/>
    <path d="M0 44 C110 22 230 58 398 36 L398 172 L0 172Z" fill="url(#g1)"/>
    <path d="M0 100 C140 76 260 118 398 90 L398 172 L0 172Z" fill="#4a6d16" opacity=".35"/>
  </svg>
  <div class="headline">Pilzkulturen &amp; Zubehör</div>
  <div class="subline">für Pilzzüchter</div>
  <div class="badge" style="left:334px;top:86px"><span>NEUKUNDEN-<br>RABATT SICHERN!</span></div>
</section>

<section class="card" style="left:652px;top:144px">
  <div class="brand"><span class="brand-dot"></span>moosgarten-kultur.shop</div>
  <p class="intro" style="top:72px">Wir sind spezialisiert auf exotische und rare Pilzzucht-Produkte, die Sie meist so nirgends erhalten. Wir führen Pilzbrut für die Ansiedelung von Waldpilzen in Ihrem Garten- oder Waldstück, aber auch klassische Pilzsorten für den Anbau im Haus.</p>
  <p class="intro" style="top:176px">Ergänzt wird unser Sortiment durch verschiedene Substrate und Substratbeutel und hilfreiches Zubehör für die Zucht und für die Vermehrung von Pilzkulturen.</p>
  <div class="tile tile--sets" role="img" aria-label="Fertigzuchtset mit Austernpilzen"></div>
  <div class="tag" style="left:230px;top:115px">Fertigzuchtsets</div>
  <div class="badge" style="left:249px;top:235px;width:76px;height:76px;margin:-38px 0 0 -38px"><span style="font-size:18px">NACH<br>8 TAGEN</span></div>
  <div class="tile tile--substrate" role="img" aria-label="Hände halten Pilzsubstrat"></div>
  <div class="tag" style="left:34px;top:264px">Substrat &amp; Zubehör</div>
  <div class="tile tile--garden" role="img" aria-label="Steinpilz im Waldboden"></div>
  <div class="tag" style="left:230px;top:483px">Garten &amp; Waldzucht</div>
  <div class="offer">XX% NEUKUNDEN-<br>RABATT SICHERN!</div>
  <p class="offer-terms">Den Code XXXXXX im Bestellformular eingeben und XX% Rabatt auf die erste Bestellung erhalten (ab XX € Mindestbestellwert)</p>
</section>

<div class="variant-label" style="left:162px;top:731px">Variante 1</div>

<div class="sheet-divider"></div>

<h2 class="section-title" style="top:893px">Varianten Vorderseite</h2>

<section class="card" style="left:162px;top:1017px">
  <div class="brand"><span class="brand-dot"></span>moosgarten-kultur.shop</div>
  <div class="photo photo--shimeji" role="img" aria-label="Buchenpilze auf hellbraunem Grund"></div>
  <svg class="meadow" viewBox="0 0 398 172" preserveAspectRatio="none" aria-hidden="true">
    <defs><linearGradient id="g2" x1="0" y1="0" x2="0" y2="1"><stop offset="0" stop-color="#8db236"/><stop offset="1" stop-color="#4a6d16"/></linearGradient></defs>
    <path d="M0 12 C90 -4 170 28 260 16 C320 8 370 6 398 12 L398 172 L0 172Z" fill="url(#g2)" opacity=".82"/>
    <path d="M0 44 C110 22 230 58 398 36 L398 172 L0 172Z" fill="url(#g2)"/>
    <path d="M0 100 C140 76 260 118 398 90 L398 172 L0 172Z" fill="#4a6d16" opacity=".35"/>
  </svg>
  <div class="headline">Pilzkulturen &amp; Zubehör</div>
  <div class="subline">für Pilzzüchter</div>
  <div class="badge" style="left:334px;top:86px"><span>NEUKUNDEN-<br>RABATT SICHERN!</span></div>
</section>

<section class="card" style="left:652px;top:1017px">
  <div class="brand"><span class="brand-dot"></span>moosgarten-kultur.shop</div>
  <div class="photo photo--forest" role="img" aria-label="Hand hält frisch gesammelten Pilz im Wald"></div>
  <svg class="meadow" viewBox="0 0 398 172" preserveAspectRatio="none" aria-hidden="true">
    <defs><linearGradient id="g3" x1="0" y1="0" x2="0" y2="1"><stop offset="0" stop-color="#8db236"/><stop offset="1" stop-color="#4a6d16"/></linearGradient></defs>
    <path d="M0 12 C90 -4 170 28 260 16 C320 8 370 6 398 12 L398 172 L0 172Z" fill="url(#g3)" opacity=".82"/>
    <path d="M0 44 C110 22 230 58 398 36 L398 172 L0 172Z" fill="url(#g3)"/>
    <path d="M0 100 C140 76 260 118 398 90 L398 172 L0 172Z" fill="#4a6d16" opacity=".35"/>
  </svg>
  <div class="headline">Pilzkulturen &amp; Zubehör</div>
  <div class="subline">für Pilzzüchter</div>
  <div class="badge" style="left:334px;top:86px"><span>NEUKUNDEN-<br>RABATT SICHERN!</span></div>
</section>

<div class="variant-label" style="left:162px;top:1603px">Variante 1</div>
<div class="variant-label" style="left:652px;top:1603px">Variante 2</div>

<section class="card" style="left:162px;top:1711px">
  <div class="brand brand--right"><span class="brand-dot"></span>moosgarten-kultur.shop</div>
  <div class="photo photo--chanterelle" role="img" aria-label="Pfifferlinge in offenen Händen"></div>
  <svg class="meadow" viewBox="0 0 398 172" preserveAspectRatio="none" aria-hidden="true">
    <defs><linearGradient id="g4" x1="0" y1="0" x2="0" y2="1"><stop offset="0" stop-color="#8db236"/><stop offset="1" stop-color="#4a6d16"/></linearGradient></defs>
    <path d="M0 12 C90 -4 170 28 260 16 C320 8 370 6 398 12 L398 172 L0 172Z" fill="url(#g4)" opacity=".82"/>
    <path d="M0 44 C110 22 230 58 398 36 L398 172 L0 172Z" fill="url(#g4)"/>
    <path d="M0 100 C140 76 260 118 398 90 L398 172 L0 172Z" fill="#4a6d16" opacity=".35"/>
  </svg>
  <div class="headline">Pilzkulturen &amp; Zubehör</div>
  <div class="subline">für Pilzzüchter</div>
  <div class="badge" style="left:71px;top:370px"><span>NEUKUNDEN-<br>RABATT SICHERN!</span></div>
</section>

<section class="card" style="left:652px;top:1711px">
  <div class="brand brand--right"><span class="brand-dot"></span>moosgarten-kultur.shop</div>
  <div class="photo photo--oyster" role="img" aria-label="Person hält großen Austernpilz-Büschel vor sich"></div>
  <svg class="meadow" viewBox="0 0 398 172" preserveAspectRatio="none" aria-hidden="true">
    <defs><linearGradient id="g5" x1="0" y1="0" x2="0" y2="1"><stop offset="0" stop-color="#8db236"/><stop offset="1" stop-color="#4a6d16"/></linearGradient></defs>
    <path d="M0 12 C90 -4 170 28 260 16 C320 8 370 6 398 12 L398 172 L0 172Z" fill="url(#g5)" opacity=".82"/>
    <path d="M0 44 C110 22 230 58 398 36 L398 172 L0 172Z" fill="url(#g5)"/>
    <path d="M0 100 C140 76 260 118 398 90 L398 172 L0 172Z" fill="#4a6d16" opacity=".35"/>
  </svg>
  <div class="headline">Pilzkulturen &amp; Zubehör</div>
  <div class="subline">für Pilzzüchter</div>
  <div class="badge" style="left:70px;top:102px"><span>NEUKUNDEN-<br>RABATT SICHERN!</span></div>
</section>

<div class="variant-label" style="left:162px;top:2303px">Variante 3</div>
<div class="variant-label" style="left:652px;top:2303px">Variante 4 (bitte Bildrechte<br>und Bildbearbeitung abklären,<br>Original-Foto nötig)</div>

</body>
</html>
```